Design for Broadband Data Consumption Calculator

Primary Inspiration: http://www.quolentra-mobile.example/b2c/splash/datacalculatorPopup.jsp
This is the functionality we are looking for, but we want to use the design colors from our current site on NetKikkerten.dk
Secondary Inspiration: http://www.vimbo.dk/Privat/Mobil/Databeregner/#dc
Description
This will be a list of questions (three part, where the third part is the presentation of the price chart) that will enable us to present a list of mobile broadband providers that is suited for their needs.
Mock Up provided as well as thorough project description
Look and feel
Each slider illustrates characteristics of the customer's brand and the style your logo design should communicate.

```html
<!DOCTYPE html>
<html lang="en">
<head>
<meta charset="utf-8">
<title>Mobile Broadband Data Calculator</title>
<link rel="stylesheet" href="https://fonts.googleapis.com/css2?family=Arimo:wght@400;700&display=swap">
<style>
  :root {
    --ink: #111111;
    --muted: #6b6b6b;
    --option-active: #6d5f86;
    --rule: #dcdcdc;
    --fill-top: #e8f55a;
    --fill-bottom: #c8e000;
    --track-top: #f1f5f2;
    --track-bottom: #dfe8e3;
    --knob-ring: #2fb8b4;
    --knob-top: #eafcfc;
    --knob-bottom: #b5e6e8;
    --page: #ffffff;
  }
  * { box-sizing: border-box; margin: 0; padding: 0; }
  html, body {
    width: 1200px; height: 901px; overflow: hidden;
    background: var(--page);
    font-family: "Arimo", Arial, sans-serif;
    color: var(--ink);
  }
  .calculator {
    position: absolute; left: 0; top: 0;
    width: 650px; height: 488px;
    transform: scale(1.8462);
    transform-origin: 0 0;
  }
  .calculator-title {
    position: absolute; left: 68px; top: 19px;
    font-size: 17px; font-weight: 700;
  }
  .divider {
    position: absolute; left: 66px; width: 505px; height: 1px;
    background: var(--rule);
  }
  .section-icon { position: absolute; }
  .section-heading {
    position: absolute; left: 105px;
    font-size: 13px; font-weight: 700;
  }
  .points {
    position: absolute; right: 82px; top: 65px;
    font-size: 13px; font-weight: 700;
  }
  .question {
    position: absolute; left: 68px;
    font-size: 12px; font-weight: 700;
  }
  .slider {
    position: absolute; left: 67px; width: 389px; height: 29px;
    border-radius: 6px;
    background: linear-gradient(var(--track-top), var(--track-bottom));
  }
  .slider-fill {
    position: absolute; left: 0; top: 0; bottom: 0;
    border-radius: 6px 0 0 6px;
    background: linear-gradient(var(--fill-top), var(--fill-bottom));
  }
  .slider-option {
    position: absolute; top: 50%; transform: translate(-50%, -50%);
    font-size: 11px; font-weight: 700; color: var(--muted);
    text-align: center; line-height: 1.0;
  }
  .slider-option.is-chosen { color: var(--option-active); }
  .slider-knob {
    position: absolute; top: 50%; width: 34px; height: 34px;
    transform: translate(-50%, -50%);
    border-radius: 50%;
    border: 1.5px solid var(--knob-ring);
    background: radial-gradient(circle at 40% 35%, var(--knob-top), var(--knob-bottom));
  }
</style>
</head>
<body>
<main class="calculator">
  <h1 class="calculator-title">What device do you need mobile broadband for?</h1>
  <div class="divider" style="top:45px"></div>

  <svg class="section-icon" style="left:70px;top:54px" width="22" height="27" viewBox="0 0 22 27" aria-hidden="true">
    <path d="M7 2c-2 2 2 3 0 6M11 1c-2 2 2 3 0 6" stroke="#111" stroke-width="1.4" fill="none"/>
    <path d="M2 11h14v9a4 4 0 0 1-4 4H6a4 4 0 0 1-4-4z" fill="#111"/>
    <path d="M16 13h2a3 3 0 0 1 0 6h-2" stroke="#111" stroke-width="2" fill="none"/>
    <rect x="0" y="25" width="18" height="2" fill="#111"/>
  </svg>
  <h2 class="section-heading" style="top:65px">How often are you online?</h2>
  <span class="points">1 point</span>

  <div class="slider" style="top:106px">
    <div class="slider-fill" style="width:81px"></div>
    <span class="slider-option is-chosen" style="left:34px">Twice<br>/week</span>
    <span class="slider-option" style="left:136px">Everyday</span>
    <span class="slider-option" style="left:244px">Multiple<br>times/day</span>
    <span class="slider-option" style="left:345px">All day</span>
    <span class="slider-knob" style="left:81px"></span>
  </div>

  <div class="divider" style="top:164px"></div>

  <svg class="section-icon" style="left:72px;top:185px" width="22" height="22" viewBox="0 0 22 22" aria-hidden="true">
    <path d="M11 0v11" stroke="#111" stroke-width="3"/>
    <path d="M5 8l6 7 6-7z" fill="#111"/>
    <path d="M1 14v6h20v-6" stroke="#111" stroke-width="2.5" fill="none"/>
  </svg>
  <h2 class="section-heading" style="top:190px">What are you going to use your mobile broadband for?</h2>

  <p class="question" style="top:231px">Surfing, reading articles, netbanking</p>
  <div class="slider" style="top:260px">
    <div class="slider-fill" style="width:260px"></div>
    <span class="slider-option" style="left:61px">Never</span>
    <span class="slider-option is-chosen" style="left:195px">Sometimes</span>
    <span class="slider-option" style="left:324px">Often</span>
    <span class="slider-knob" style="left:260px"></span>
  </div>

  <p class="question" style="top:311px">Sending emails (with photos)</p>
  <div class="slider" style="top:340px">
    <div class="slider-fill" style="width:130px"></div>
    <span class="slider-option is-chosen" style="left:61px">Never</span>
    <span class="slider-option" style="left:195px">Sometimes</span>
    <span class="slider-option" style="left:324px">Often</span>
    <span class="slider-knob" style="left:130px"></span>
  </div>

  <p class="question" style="top:391px">Watching videos online (Vidora, Strimla.dk, etc.)</p>
  <div class="slider" style="top:420px">
    <div class="slider-fill" style="width:130px"></div>
    <span class="slider-option is-chosen" style="left:61px">Never</span>
    <span class="slider-option" style="left:195px">Sometimes</span>
    <span class="slider-option" style="left:324px">Often</span>
    <span class="slider-knob" style="left:130px"></span>
  </div>
</main>
</body>
</html>
```